Flooring Company Stationery Design Project

I need Business card, presentation folder, letterhead and envelope design.
I want the design to show a lot of creativity and that it has a modern look but still professional.
The company has a retail store but we specialize in in-home shopping.

Design must have a "flooring" company style. Creativity is going to be the main thing we'll be looking for. We want something that will stand out of the competition.

We are a remodeling busines and we want to look like one but with a good look.

PLEASE USE FOLLOWING LINK FOR ANY PHOTOS NEEDED
http://www.velmorta.com/syndicate/logos/choose_brands.html
Updates

PLEASE USE ANY PHOTOS NEEDED FROM HERE

Target Market(s)

Our target customer are 35-50 years old and decision makers are usually women

Industry/Entity Type

Retail

Requirements
Must have
• Color red
PHOTOS NEEDED CAN BE USED FROM HERE

```html
<!DOCTYPE html>
<html lang="en">
<head>
<meta charset="utf-8">
<title>Plankhaven Business Card</title>
<link rel="stylesheet" href="https://fonts.googleapis.com/css2?family=Lato:wght@400;700;900&display=swap">
<style>
  :root {
    --bg: #e4e4e4;
    --paper: #f7f7f5;
    --brand-red: #d8333a;
    --brand-orange: #e08a2a;
    --brand-green: #1f9a72;
    --ink: #2a2a2a;
    --ink-soft: #555555;
    --white: #ffffff;
  }
  * { box-sizing: border-box; margin: 0; padding: 0; }
  html, body { width: 1200px; height: 747px; overflow: hidden; }
  body {
    background: var(--bg);
    font-family: "Lato", sans-serif;
    position: relative;
  }
  .card {
    position: absolute;
    top: 84px;
    width: 330px;
    height: 578px;
    overflow: hidden;
    box-shadow: 0 6px 18px rgba(0,0,0,0.18);
  }
  .card--front { left: 225px; background: var(--paper); }
  .card--back { left: 645px; background: var(--brand-red); }

  .person { position: absolute; left: 40px; top: 42px; color: var(--ink); }
  .person__name { font-size: 24px; font-weight: 400; }
  .person__title { font-size: 14px; letter-spacing: 0.5px; margin-top: 2px; }

  .contact { position: absolute; left: 30px; top: 126px; list-style: none; }
  .contact__item {
    display: flex; align-items: center; gap: 10px;
    font-size: 16px; color: var(--ink); line-height: 22px;
  }
  .contact__icon { width: 14px; height: 14px; flex: none; }

  .address { position: absolute; left: 30px; top: 230px; font-size: 17px; line-height: 23px; color: var(--ink); font-style: normal; }
  .address__web { font-weight: 700; }

  .lockup { position: absolute; left: 30px; top: 418px; }
  .lockup__name {
    font-size: 44px; font-weight: 900; color: var(--brand-red);
    letter-spacing: -1px; line-height: 1.1;
  }
  .lockup__slogan {
    font-size: 13px; font-weight: 400; color: var(--ink-soft);
    letter-spacing: 1px; text-transform: uppercase; margin-top: 4px;
  }

  .stripes { position: absolute; display: flex; }
  .stripes span { display: block; width: 28px; height: 46px; }
  .stripes--front { left: 118px; bottom: 0; }
  .stripes--back { right: 46px; top: 34px; gap: 30px; }
  .stripes--back span { height: 34px; width: 30px; }
  .s-orange { background: var(--brand-orange); }
  .s-red { background: var(--brand-red); }
  .s-green { background: var(--brand-green); }

  .back-brand {
    position: absolute; left: 50%; top: 52%;
    transform: translate(-50%, -50%) rotate(-90deg);
    text-align: left; color: var(--white); white-space: nowrap;
  }
  .back-brand__name { font-size: 78px; font-weight: 900; letter-spacing: -2px; line-height: 1; }
  .back-brand__slogan { font-size: 16px; font-weight: 400; letter-spacing: 1.5px; text-transform: uppercase; margin-top: 8px; }
</style>
</head>
<body>
  <section class="card card--front">
    <div class="person">
      <h1 class="person__name">Lena Hartwell</h1>
      <p class="person__title">OPERATION MANAGER</p>
    </div>
    <ul class="contact">
      <li class="contact__item">
        <svg class="contact__icon" viewBox="0 0 14 14"><path d="M3 1l3 3-1.5 1.5a8 8 0 0 0 4 4L10 8l3 3-2 2C6 13 1 8 1 3z" fill="var(--brand-red)"/></svg>
        +1 555 014 2738
      </li>
      <li class="contact__item">
        <svg class="contact__icon" viewBox="0 0 14 14"><rect x="3" y="1" width="8" height="12" rx="1" fill="none" stroke="var(--brand-orange)" stroke-width="1.5"/><rect x="5" y="3" width="4" height="4" fill="var(--brand-orange)"/></svg>
        +61 400 555 019
      </li>
      <li class="contact__item">
        <svg class="contact__icon" viewBox="0 0 14 14"><rect x="1" y="3" width="12" height="8" fill="none" stroke="var(--brand-green)" stroke-width="1.3"/><path d="M1 3l6 5 6-5" fill="none" stroke="var(--brand-green)" stroke-width="1.3"/></svg>
        name@plankhaven.com
      </li>
    </ul>
    <address class="address">
      48 Alder Row,<br>
      Fairmont, Ontario K2P 4B9<br>
      <span class="address__web">www.plankhaven.com</span>
    </address>
    <div class="lockup">
      <div class="lockup__name">plankhaven</div>
      <p class="lockup__slogan">Floors Made For Everyday Living</p>
    </div>
    <div class="stripes stripes--front"><span class="s-orange"></span><span class="s-red"></span><span class="s-green"></span></div>
  </section>

  <section class="card card--back">
    <div class="stripes stripes--back"><span class="s-orange"></span><span class="s-green"></span></div>
    <div class="back-brand">
      <div class="back-brand__name">plankhaven</div>
      <div class="back-brand__slogan">Floors Made For Everyday Living</div>
    </div>
  </section>
</body>
</html>
```